DOG DAYCARE BILLBOARD

Design a bold exciting billboard that can be read easily from a distance! Our goal is brand awareness and showcasing the services we offer (Boarding, Grooming, Daycare, and Training.
we would like to see examples with the phrase "your best friend's best day". Our name Bright Meadow Canine Activity Center (or just Bright Meadow might work better and could be bigger) and the services we provide.
(there are two examples of what we like included in the pictures)
you can find more information o our website at pawplayhub@mailnest.example.

```html
<!DOCTYPE html>
<html lang="en">
<head>
<meta charset="utf-8">
<title>Bright Meadow Billboard</title>
<link rel="stylesheet" href="https://fonts.googleapis.com/css2?family=Montserrat:wght@400;500&family=Rubik:wght@400;700;900&display=swap">
<style>
  :root {
    --page: #e4e4e2;
    --lime: #cbd94b;
    --green: #3aa431;
    --green-deep: #2f8f2a;
    --charcoal: #2c2c2c;
    --ink: #1e1e1e;
    --paper: #ffffff;
    --silver: #ececec;
    --tone-gold: #c9955a;
    --tone-cream: #e9d3bb;
    --tone-rose: #c98f86;
    --tone-sky: #9fb8c9;
  }
  * { box-sizing: border-box; margin: 0; padding: 0; }
  html, body { width: 1200px; height: 750px; overflow: hidden; background: var(--page); }
  .billboard {
    position: absolute; left: 30px; top: 128px; width: 1140px; height: 494px;
    overflow: hidden; background: var(--charcoal);
    font-family: "Rubik", sans-serif;
  }
  .headline-band {
    position: absolute; left: 0; top: 0; width: 100%; height: 190px;
    background: linear-gradient(90deg, var(--lime) 0%, #a9cf41 45%, var(--green) 100%);
  }
  .brand-mark {
    position: absolute; left: 60px; top: 72px; display: flex; align-items: center; gap: 12px;
    font-family: "Rubik", sans-serif; font-weight: 700; font-size: 30px; color: var(--ink);
  }
  .brand-mark .dot { width: 26px; height: 26px; border-radius: 50%; background: var(--ink); }
  .tagline {
    position: absolute; right: 72px; top: 24px;
    font-weight: 900; font-size: 42px; color: var(--ink); letter-spacing: 0.5px; white-space: nowrap;
  }
  .business-name {
    position: absolute; right: 70px; top: 66px;
    font-weight: 700; font-size: 84px; line-height: 1; color: var(--silver); white-space: nowrap;
    letter-spacing: 1px;
  }
  .location {
    position: absolute; right: 72px; top: 156px;
    font-weight: 400; font-size: 29px; color: var(--ink);
  }
  .services { position: absolute; left: 56px; top: 216px; display: flex; gap: 30px; }
  .service { width: 196px; display: flex; flex-direction: column; align-items: center; gap: 10px; }
  .service-label {
    font-family: "Montserrat", sans-serif; font-weight: 500; font-size: 27px; letter-spacing: 3px;
    color: var(--paper); white-space: nowrap;
  }
  .service-frame {
    width: 196px; height: 150px; background: var(--paper);
    clip-path: polygon(0 0, 100% 0, 100% 72%, 78% 100%, 22% 100%, 0 72%);
    padding: 6px;
  }
  .service-photo {
    width: 100%; height: 100%;
    clip-path: polygon(0 0, 100% 0, 100% 72%, 78% 100%, 22% 100%, 0 72%);
  }
  .photo-boarding { background: radial-gradient(circle at 50% 55%, var(--tone-gold), #8c6a48); }
  .photo-grooming { background: radial-gradient(circle at 45% 50%, var(--tone-cream), var(--tone-rose)); }
  .photo-daycare { background: radial-gradient(circle at 50% 55%, var(--tone-cream), var(--tone-sky)); }
  .photo-training { background: radial-gradient(circle at 50% 50%, var(--tone-gold), #d9c7ad); }
  .web-address {
    position: absolute; left: 0; width: 1080px; top: 408px; text-align: center;
    font-family: "Montserrat", sans-serif; font-size: 22px; color: var(--paper);
  }
  .footer-band {
    position: absolute; left: 0; top: 444px; width: 100%; height: 50px;
    background: linear-gradient(90deg, var(--green) 0%, #7cc43a 50%, var(--lime) 100%);
    border-top: 14px solid var(--green-deep);
  }
  .chevrons { position: absolute; right: 0; top: 190px; display: block; }
</style>
</head>
<body>
  <main class="billboard">
    <section class="headline-band">
      <div class="brand-mark"><span class="dot"></span>Bright Meadow</div>
      <p class="tagline">YOUR BEST FRIEND'S BEST DAY</p>
      <h1 class="business-name">BRIGHT MEADOW</h1>
      <p class="location">Maple Hollow IA</p>
    </section>

    <section class="services">
      <div class="service">
        <span class="service-label">BOARDING</span>
        <div class="service-frame"><div class="service-photo photo-boarding" role="img" aria-label="Photo of a golden dog resting its head"></div></div>
      </div>
      <div class="service">
        <span class="service-label">GROOMING</span>
        <div class="service-frame"><div class="service-photo photo-grooming" role="img" aria-label="Photo of a groomed spaniel holding a pink flower"></div></div>
      </div>
      <div class="service">
        <span class="service-label">DAYCARE</span>
        <div class="service-frame"><div class="service-photo photo-daycare" role="img" aria-label="Photo of a person hugging a pug"></div></div>
      </div>
      <div class="service">
        <span class="service-label">TRAINING</span>
        <div class="service-frame"><div class="service-photo photo-training" role="img" aria-label="Photo of a golden retriever with a blue ball"></div></div>
      </div>
    </section>

    <p class="web-address">pawplayhub.example</p>
    <div class="footer-band"></div>

    <svg class="chevrons" width="180" height="254" viewBox="0 0 180 254" aria-hidden="true">
      <defs>
        <linearGradient id="chevron-green" x1="0" y1="0" x2="0" y2="1">
          <stop offset="0" stop-color="#3aa431"/>
          <stop offset="1" stop-color="#cbd94b"/>
        </linearGradient>
        <clipPath id="chevron-clip"><rect width="180" height="254"/></clipPath>
      </defs>
      <g clip-path="url(#chevron-clip)" fill="none" stroke="url(#chevron-green)" stroke-width="18" stroke-linejoin="miter">
        <polyline points="200,-10 14,127 200,264"/>
        <polyline points="200,48 92,127 200,206"/>
        <polyline points="200,96 156,127 200,158"/>
      </g>
    </svg>
  </main>
</body>
</html>
```